Modern, cutting edge crypto trading website.

I need a single-page website design, approximate 4-5 pages. I have included a screenshot of the inside of the current application for some reference for what it currently looks like. This is the public side of the application for not logged in users.

I am currently thinking about 3-5 sections of the page.
Menu at top is optional, these could be the sections of the site.
1. Above the fold cool, grabbing stuff.
2. What problem does this solve
3. Additional benefits
4. Pricing
5. Open to ideas! Well it's all open to ideas if you have ideas.

I am nervous about hiring designers, I am open to a further discussion for more work for additional money but I have to LIKE your design. So this could be considered a trial. I would like to continue to design the application itself and match everything together!

I really like the trendkite website.

Competitor websites:
https://7pillars.example/
https://www.trendkite.example/

Target Market(s)

Adults 25-50 mostly male,

Number of Pages Required

4 page

Colors

Designer to choose colors to be used in the design.

Requirements
Must have
• Modern design, clean lines, professional.
Nice to have
• Fun SVG stuff. Not for this price, but in the future.
Should not have
• Should not be cluttered OR too spacey. Quorble's website has too much open space sometimes.

```html
<!DOCTYPE html>
<html lang="en">
<head>
<meta charset="utf-8">
<title>Coinvale — Learn The Power Of The Crypto's</title>
<link rel="stylesheet" href="https://fonts.googleapis.com/css2?family=Montserrat:wght@400;500;600;700;800;900&display=swap">
<style>
:root{
  --hero:#2839b2;
  --section:#2233aa;
  --section-alt:#2031a6;
  --panel:#0a0d50;
  --pricing-bg:#0d1062;
  --row:#2538ab;
  --label:#8f9ad8;
  --accent:#45d6f2;
  --white:#ffffff;
  --muted:#c4cbf2;
  --faint:#7f8ad4;
  --ghost:rgba(255,255,255,0.05);
  --font:'Montserrat',sans-serif;
}
*{margin:0;padding:0;box-sizing:border-box}
html,body{width:1200px;height:3703px;overflow:hidden}
body{font-family:var(--font);color:var(--white);background:var(--section);position:relative}
section{position:absolute;left:0;width:1200px;overflow:hidden}

/* hero */
.hero{top:0;height:568px;background:var(--hero)}
.hero-art{position:absolute;left:190px;top:170px;width:760px;height:350px;border-radius:30px;
  background:radial-gradient(ellipse at center,rgba(80,110,220,.45),rgba(40,57,178,0) 70%)}
.nav{position:absolute;top:30px;left:161px;width:878px;height:52px;display:flex;align-items:center;white-space:nowrap}
.brand{display:flex;align-items:center;gap:9px;font-weight:700;font-size:12.5px}
.brand-dot{width:52px;height:52px;border-radius:50%;background:var(--white)}
.menu{display:flex;gap:22px;margin-left:36px;font-size:11px;font-weight:500}
.menu a{color:var(--white);text-decoration:none;white-space:nowrap}
.menu a.active{color:var(--accent);border-bottom:1px solid var(--accent);padding-bottom:3px}
.nav-btns{margin-left:auto;display:flex;gap:15px}
.btn{display:inline-flex;align-items:center;justify-content:center;font-weight:700;font-size:11.5px;text-decoration:none;white-space:nowrap}
.btn-login{width:105px;height:36px;background:var(--white);color:var(--accent)}
.btn-signup{width:105px;height:36px;background:var(--accent);color:var(--white)}
.hero h1{position:absolute;top:178px;left:0;width:1200px;text-align:center;font-size:38px;font-weight:900;line-height:47px;letter-spacing:1px}
.hero p{position:absolute;top:298px;left:300px;width:600px;text-align:center;font-size:12.5px;line-height:23px;font-weight:500}
.btn-hero{position:absolute;top:370px;left:520px;width:158px;height:54px;background:var(--accent);color:var(--white);font-size:12px}

/* section heads */
.ghost{position:absolute;left:0;width:1200px;text-align:center;font-weight:900;font-size:100px;color:var(--ghost);letter-spacing:4px}
.sec-title{position:absolute;left:0;width:1200px;text-align:center;font-size:22px;font-weight:700}
.sec-desc{position:absolute;left:240px;width:720px;text-align:center;font-size:10.5px;line-height:22px;font-weight:500}

/* benefits */
.benefits{top:568px;height:960px;background:var(--section)}
.card{position:absolute;top:241px;width:278px;height:318px;border:1px solid rgba(255,255,255,.35);text-align:center}
.card .icon{margin:45px auto 0;width:100px;height:90px;border-radius:8px;background:linear-gradient(135deg,rgba(69,214,242,.35),rgba(69,214,242,.08))}
.card h3{margin-top:32px;font-size:13.5px;font-weight:700}
.rule{width:36px;height:2px;background:var(--accent);margin:22px auto 0}
.card p{margin:22px auto 0;width:230px;font-size:10.5px;line-height:22px;color:var(--muted)}
.intro{position:absolute;top:610px;left:161px;width:440px;font-size:9.5px;line-height:20px;color:var(--faint)}
.steps{position:absolute;top:726px;left:196px;list-style:none}
.steps li{display:flex;gap:14px;font-size:10px;line-height:22px;width:340px;margin-bottom:2px}
.steps b{color:var(--accent);font-size:19px;font-weight:800;width:16px;line-height:26px;flex:none}
.cycle{position:absolute;top:618px;left:690px;width:320px;height:290px;border-radius:50%;
  background:radial-gradient(circle,rgba(69,214,242,.28),rgba(69,214,242,.06) 70%)}

/* problems */
.problems{top:1528px;height:640px;background:var(--section-alt)}
.prob-panel{position:absolute;top:240px;left:161px;width:878px;height:353px;background:var(--panel)}
.prob{position:absolute;width:370px}
.prob .pic{position:absolute;left:0;top:0;width:48px;height:48px;border-radius:8px;background:linear-gradient(135deg,#4a6be0,#45d6f2)}
.prob h4{margin-left:70px;font-size:14.5px;font-weight:700}
.prob ul{margin:12px 0 0 70px;list-style:none}
.prob li{position:relative;padding-left:19px;font-size:9px;line-height:22px;color:var(--muted)}
.prob li::before{content:"";position:absolute;left:0;top:8px;width:7px;height:7px;border-radius:50%;background:var(--accent)}

/* solutions */
.solutions{top:2168px;height:663px;background:var(--section-alt)}
.sol{position:absolute;width:200px;text-align:center}
.sol .pic{margin:0 auto;width:60px;height:60px;border-radius:50%;background:linear-gradient(135deg,rgba(69,214,242,.45),rgba(69,214,242,.1))}
.sol h3{margin-top:22px;font-size:15px;font-weight:700}
.sol .rule{margin-top:20px}
.sol p{margin-top:18px;font-size:10.5px;line-height:22px;color:var(--muted)}

/* pricing */
.pricing{top:2831px;height:569px;background:var(--pricing-bg)}
.plan{position:absolute;left:161px;width:878px;height:97px;background:var(--row)}
.plan-label{position:absolute;left:0;top:0;width:203px;height:97px;background:var(--label)}
.plan-label .name{position:absolute;left:22px;top:18px;font-size:12.5px;font-weight:700}
.plan-label .slash{position:absolute;left:98px;top:34px;font-size:22px;font-weight:300}
.plan-label .price{position:absolute;left:132px;top:45px;font-size:15px;font-weight:700}
.plan-label .per{position:absolute;left:132px;top:66px;font-size:9px}
.feat{position:absolute;left:247px;top:28px;display:grid;grid-template-columns:repeat(4,115px);row-gap:10px;font-size:10.5px}
.feat span{display:flex;align-items:center;gap:8px;white-space:nowrap}
.feat span.off{opacity:.35}
.feat svg{width:12px;height:10px}
.plan-btn{position:absolute;left:727px;top:29px;width:104px;height:38px;border:2px solid var(--white);color:var(--white);font-size:11px}
.plan-btn.filled{background:var(--accent);border-color:var(--accent)}

/* contact */
.contact{top:3400px;height:303px;background:var(--section)}
.contact h2{position:absolute;left:161px;top:56px;font-size:22px;font-weight:700}
.contact .lead{position:absolute;left:161px;top:93px;width:200px;font-size:9.5px;line-height:22px;color:var(--muted)}
.socials{position:absolute;left:161px;top:163px;display:flex;gap:23px}
.socials span{width:22px;height:22px;border-radius:50%;background:var(--white)}
.copy{position:absolute;left:161px;top:219px;font-size:9.5px}
.field{position:absolute;border:1px solid rgba(255,255,255,.5);font-size:9.5px;font-style:italic;color:var(--muted);padding:8px 11px}
.send{position:absolute;left:548px;top:201px;width:104px;height:37px;background:var(--accent);font-size:11.5px;color:var(--white)}
.mailbox{position:absolute;left:841px;top:75px;width:198px;height:165px;border-radius:20px;background:linear-gradient(160deg,rgba(69,140,242,.55),rgba(69,214,242,.15))}
</style>
</head>
<body>

<section class="hero">
  <div class="hero-art" role="img" aria-label="Isometric crypto mining illustration with coins and server blocks"></div>
  <nav class="nav">
    <div class="brand"><span class="brand-dot"></span>Coinvale</div>
    <div class="menu">
      <a class="active" href="#">HOME</a><a href="#">ABOUT</a><a href="#">SERVICES</a><a href="#">BENEFITS</a><a href="#">HOW IT WORKS</a><a href="#">CONTACT US</a>
    </div>
    <div class="nav-btns"><a class="btn btn-login" href="#">LOGIN</a><a class="btn btn-signup" href="#">SIGN UP</a></div>
  </nav>
  <h1>Learn The Power Of<br>The Crypto's</h1>
  <p>Lorem ipsum dolor amet post-ironic kickstarter he brooklyn trust fund synth poke. Ennui0 pok pok lumbersexual bespoke, listicle tofu live-edge hell of palo santo hot chick</p>
  <a class="btn btn-hero" href="#">DISCOVER MORE</a>
</section>

<section class="benefits">
  <div class="ghost" style="top:27px">BENEFITS</div>
  <h2 class="sec-title" style="top:74px">What Are The Benefits &amp; How It Works?</h2>
  <p class="sec-desc" style="top:150px">Fingerstache snackwave ennui mumblecore +1 meh blog shoreditch and mustache occupy before they sold out YOLO. Chambray pickled taiyaki man bun hammock aesthetic hoodie yr chia snackwave succulents microdosing direct trade</p>

  <div class="card" style="left:161px"><div class="icon" role="img" aria-label="Trading desk illustration"></div><h3>Lorem Ipsum Dolor</h3><div class="rule"></div><p>Cardigan pour-over forage selfies and gochu-jang. Godard messenger bag isan post-ironic lorem ipsum dolor</p></div>
  <div class="card" style="left:461px"><div class="icon" role="img" aria-label="Document and coin illustration"></div><h3>Lorem Ipsum Dolor Amet</h3><div class="rule"></div><p>Cardigan pour-over forage selfies and gochu-jang. Godard messenger bag isan post-ironic lorem ipsum dolor</p></div>
  <div class="card" style="left:761px"><div class="icon" role="img" aria-label="Orbiting coin illustration"></div><h3>Simply Dummy Text</h3><div class="rule"></div><p>Cardigan pour-over forage selfies and gochu-jang. Godard messenger bag isan post-ironic lorem ipsum dolor</p></div>

  <p class="intro">At vero eos et accusamus et iusto odio dignissimos ducimus qui blan ditiis praes entium volup tatum deleniti atque corrupti quos dolores et quas mole stias excepturi sint occas ecati cupid itate non provident, similique sunt in culpa qui officia dese runt mollitia animi, id est laborum et dolorum fuga. Et harum quidem rerum facilis est et expedita</p>
  <ol class="steps">
    <li><b>1.</b><span>At vero eos et accusamus et iusto odio dignissimos ducimus qui blan ditiis praes entium volup tatum deleniti</span></li>
    <li><b>2.</b><span>At vero eos et accusamus et iusto odio dignissimos ducimus qui blan ditiis praes entium volup tatum deleniti</span></li>
    <li><b>3.</b><span>At vero eos et accusamus et iusto odio dignissimos ducimus qui blan ditiis praes entium volup tatum deleniti</span></li>
    <li><b>4.</b><span>At vero eos et accusamus et iusto odio dignissimos ducimus qui blan ditiis praes entium volup tatum deleniti</span></li>
  </ol>
  <div class="cycle" role="img" aria-label="Circular workflow illustration of wallet, coin storage, exchange and growth chart"></div>
</section>

<section class="problems">
  <div class="ghost" style="top:20px">PROBLEMS</div>
  <h2 class="sec-title" style="top:70px">The Major Problems</h2>
  <p class="sec-desc" style="top:148px">Fingerstache snackwave ennui mumblecore +1 meh blog shoreditch and mustache occupy before they sold out YOLO. Chambray pickled taiyaki man bun hammock aesthetic hoodie yr chia snackwave succulents microdosing direct trade</p>
  <div class="prob-panel">
    <div class="prob" style="left:58px;top:55px"><div class="pic" role="img" aria-label="Trader with coins illustration"></div><h4>Lorem Ipsum</h4><ul><li>Fingerstache snackwave ennui mumblecore +1 meh blog and shoreditch mustache occupy before they sold out YOLO</li><li>Fingerstache snackwave ennui mumblecore +1 meh blog and</li></ul></div>
    <div class="prob" style="left:450px;top:55px"><div class="pic" role="img" aria-label="Stacked coins illustration"></div><h4>Simply Dummy</h4><ul><li>Fingerstache snackwave ennui mumblecore +1 meh blog and shoreditch mustache occupy before they sold out YOLO</li><li>Fingerstache snackwave ennui mumblecore +1 meh blog and</li></ul></div>
    <div class="prob" style="left:58px;top:202px"><div class="pic" role="img" aria-label="Laptop chart illustration"></div><h4>Ipsum Text</h4><ul><li>Fingerstache snackwave ennui mumblecore +1 meh blog and shoreditch mustache occupy before they sold out YOLO</li><li>Fingerstache snackwave ennui mumblecore +1 meh blog and</li></ul></div>
    <div class="prob" style="left:450px;top:202px"><div class="pic" role="img" aria-label="Network blocks illustration"></div><h4>Dolor Amet</h4><ul><li>Fingerstache snackwave ennui mumblecore +1 meh blog and shoreditch mustache occupy before they sold out YOLO</li><li>Fingerstache snackwave ennui mumblecore +1 meh blog and</li></ul></div>
  </div>
</section>

<section class="solutions">
  <div class="ghost" style="top:0">SOLUTIONS</div>
  <h2 class="sec-title" style="top:39px">What Problems We Solve?</h2>
  <p class="sec-desc" style="top:114px">Fingerstache snackwave ennui mumblecore +1 meh blog shoreditch and mustache occupy before they sold out YOLO. Chambray pickled taiyaki man bun hammock aesthetic hoodie yr chia snackwave succulents microdosing direct trade</p>

  <div class="sol" style="left:161px;top:190px"><div class="pic" role="img" aria-label="Coin in hand icon"></div><h3>Valar Portekam</h3><div class="rule"></div><p>Cardigan pour-over forage selfies gochu-jang. Godard messenger bag artisan post-ironic</p></div>
  <div class="sol" style="left:386px;top:190px"><div class="pic" role="img" aria-label="Connected cube icon"></div><h3>Valar Portekam</h3><div class="rule"></div><p>Cardigan pour-over forage selfies gochu-jang. Godard messenger bag artisan post-ironic</p></div>
  <div class="sol" style="left:611px;top:190px"><div class="pic" role="img" aria-label="Blockchain cubes icon"></div><h3>Valar Portekam</h3><div class="rule"></div><p>Cardigan pour-over forage selfies gochu-jang. Godard messenger bag artisan post-ironic</p></div>
  <div class="sol" style="left:836px;top:190px"><div class="pic" role="img" aria-label="Magnifier icon"></div><h3>Valar Portekam</h3><div class="rule"></div><p>Cardigan pour-over forage selfies gochu-jang. Godard messenger bag artisan post-ironic</p></div>

  <div class="sol" style="left:161px;top:406px"><div class="pic" role="img" aria-label="Coin group icon"></div><h3>Valar Portekam</h3><div class="rule"></div><p>Cardigan pour-over forage selfies gochu-jang. Godard messenger bag artisan post-ironic</p></div>
  <div class="sol" style="left:386px;top:406px"><div class="pic" role="img" aria-label="Circuit coin icon"></div><h3>Valar Portekam</h3><div class="rule"></div><p>Cardigan pour-over forage selfies gochu-jang. Godard messenger bag artisan post-ironic</p></div>
  <div class="sol" style="left:611px;top:406px"><div class="pic" role="img" aria-label="Mining rig icon"></div><h3>Valar Portekam</h3><div class="rule"></div><p>Cardigan pour-over forage selfies gochu-jang. Godard messenger bag artisan post-ironic</p></div>
  <div class="sol" style="left:836px;top:406px"><div class="pic" role="img" aria-label="Coin pulse icon"></div><h3>Valar Portekam</h3><div class="rule"></div><p>Cardigan pour-over forage selfies gochu-jang. Godard messenger bag artisan post-ironic</p></div>
</section>

<section class="pricing">
  <div class="ghost" style="top:28px">PRICINGS</div>
  <h2 class="sec-title" style="top:70px">Our Reasonable Pricing Tables</h2>

  <div class="plan" style="top:156px">
    <div class="plan-label"><span class="name">BASIC</span><span class="slash">/</span><span class="price">$19.99</span><span class="per">Per Month</span></div>
    <div class="feat">
      <span><svg viewBox="0 0 12 10"><path d="M1 5l3.5 3.5L11 1" stroke="#fff" stroke-width="1.6" fill="none"/></svg>Lorem Ipsum</span>
      <span><svg viewBox="0 0 12 10"><path d="M1 5l3.5 3.5L11 1" stroke="#fff" stroke-width="1.6" fill="none"/></svg>Lorem Ipsum</span>
      <span class="off"><svg viewBox="0 0 12 10"><path d="M1 5l3.5 3.5L11 1" stroke="#fff" stroke-width="1.6" fill="none"/></svg>Lorem Ipsum</span>
      <span class="off"><svg viewBox="0 0 12 10"><path d="M1 5l3.5 3.5L11 1" stroke="#fff" stroke-width="1.6" fill="none"/></svg>Lorem Ipsum</span>
      <span><svg viewBox="0 0 12 10"><path d="M1 5l3.5 3.5L11 1" stroke="#fff" stroke-width="1.6" fill="none"/></svg>Lorem Ipsum</span>
      <span><svg viewBox="0 0 12 10"><path d="M1 5l3.5 3.5L11 1" stroke="#fff" stroke-width="1.6" fill="none"/></svg>Lorem Ipsum</span>
      <span class="off"><svg viewBox="0 0 12 10"><path d="M1 5l3.5 3.5L11 1" stroke="#fff" stroke-width="1.6" fill="none"/></svg>Lorem Ipsum</span>
      <span class="off"><svg viewBox="0 0 12 10"><path d="M1 5l3.5 3.5L11 1" stroke="#fff" stroke-width="1.6" fill="none"/></svg>Lorem Ipsum</span>
    </div>
    <a class="btn plan-btn" href="#">GET IT NOW</a>
  </div>

  <div class="plan" style="top:284px">
    <div class="plan-label"><span class="name">STANDARD</span><span class="slash">/</span><span class="price">$39.99</span><span class="per">Per Month</span></div>
    <div class="feat">
      <span><svg viewBox="0 0 12 10"><path d="M1 5l3.5 3.5L11 1" stroke="#fff" stroke-width="1.6" fill="none"/></svg>Lorem Ipsum</span>
      <span><svg viewBox="0 0 12 10"><path d="M1 5l3.5 3.5L11 1" stroke="#fff" stroke-width="1.6" fill="none"/></svg>Lorem Ipsum</span>
      <span><svg viewBox="0 0 12 10"><path d="M1 5l3.5 3.5L11 1" stroke="#fff" stroke-width="1.6" fill="none"/></svg>Lorem Ipsum</span>
      <span class="off"><svg viewBox="0 0 12 10"><path d="M1 5l3.5 3.5L11 1" stroke="#fff" stroke-width="1.6" fill="none"/></svg>Lorem Ipsum</span>
      <span><svg viewBox="0 0 12 10"><path d="M1 5l3.5 3.5L11 1" stroke="#fff" stroke-width="1.6" fill="none"/></svg>Lorem Ipsum</span>
      <span><svg viewBox="0 0 12 10"><path d="M1 5l3.5 3.5L11 1" stroke="#fff" stroke-width="1.6" fill="none"/></svg>Lorem Ipsum</span>
      <span><svg viewBox="0 0 12 10"><path d="M1 5l3.5 3.5L11 1" stroke="#fff" stroke-width="1.6" fill="none"/></svg>Lorem Ipsum</span>
      <span class="off"><svg viewBox="0 0 12 10"><path d="M1 5l3.5 3.5L11 1" stroke="#fff" stroke-width="1.6" fill="none"/></svg>Lorem Ipsum</span>
    </div>
    <a class="btn plan-btn filled" href="#">GET IT NOW</a>
  </div>

  <div class="plan" style="top:411px">
    <div class="plan-label"><span class="name">PREMIUM</span><span class="slash">/</span><span class="price">$79.99</span><span class="per">Per Month</span></div>
    <div class="feat">
      <span><svg viewBox="0 0 12 10"><path d="M1 5l3.5 3.5L11 1" stroke="#fff" stroke-width="1.6" fill="none"/></svg>Lorem Ipsum</span>
      <span><svg viewBox="0 0 12 10"><path d="M1 5l3.5 3.5L11 1" stroke="#fff" stroke-width="1.6" fill="none"/></svg>Lorem Ipsum</span>
      <span><svg viewBox="0 0 12 10"><path d="M1 5l3.5 3.5L11 1" stroke="#fff" stroke-width="1.6" fill="none"/></svg>Lorem Ipsum</span>
      <span><svg viewBox="0 0 12 10"><path d="M1 5l3.5 3.5L11 1" stroke="#fff" stroke-width="1.6" fill="none"/></svg>Lorem Ipsum</span>
      <span><svg viewBox="0 0 12 10"><path d="M1 5l3.5 3.5L11 1" stroke="#fff" stroke-width="1.6" fill="none"/></svg>Lorem Ipsum</span>
      <span><svg viewBox="0 0 12 10"><path d="M1 5l3.5 3.5L11 1" stroke="#fff" stroke-width="1.6" fill="none"/></svg>Lorem Ipsum</span>
      <span><svg viewBox="0 0 12 10"><path d="M1 5l3.5 3.5L11 1" stroke="#fff" stroke-width="1.6" fill="none"/></svg>Lorem Ipsum</span>
      <span><svg viewBox="0 0 12 10"><path d="M1 5l3.5 3.5L11 1" stroke="#fff" stroke-width="1.6" fill="none"/></svg>Lorem Ipsum</span>
    </div>
    <a class="btn plan-btn" href="#">GET IT NOW</a>
  </div>
</section>

<section class="contact">
  <h2>Get In Touch</h2>
  <p class="lead">Any question? Reach out to us and we'll get back to you shortly</p>
  <div class="socials"><span></span><span></span><span></span></div>
  <p class="copy">Copyright - All Rights Reserved</p>
  <div class="field" style="left:385px;top:63px;width:204px;height:29px">Your Name</div>
  <div class="field" style="left:611px;top:63px;width:204px;height:29px">Your E-mail</div>
  <div class="field" style="left:385px;top:103px;width:430px;height:75px">Message..</div>
  <a class="btn send" href="#">SEND</a>
  <div class="mailbox" role="img" aria-label="Mailbox illustration with flying letters"></div>
</section>

</body>
</html>
```